Business Card Design Project for Architecture and Interior Design company

We need a business card design and logo for an architecture and design firm located in Santiago de Chile. It´s a small company, and the name is "Ostrevo" ("Ostr" from my surname Ostrini, and "arq" for arquitectura or architecture. But it would also be nice that the logo comunicates de Word game "Bella" as beautiful in italian, and "arq" as architecture".
The idea is to give a delicate, elegant and sofisticated, yet fresh image. Would prefer grey black and white colors, but wouldn´t mind to use another additional color.
I allready have a web page www.ostrevo-studio.example, but would like to improve the logo design.
Please contact if any further information is requiered.
Reason: Need a more arquitectural and desing spirit in the cards. Few of them give that idea.

```html
<!DOCTYPE html>
<html lang="en">
<head>
<meta charset="utf-8">
<title>Ostrevo — Business Card</title>
<link href="https://fonts.googleapis.com/css2?family=Cabin:wght@400;600;700&display=swap" rel="stylesheet">
<style>
  :root {
    --page: #ffffff;
    --ink: #1b1a17;
    --logo: #3a362f;
    --label: #2c2b28;
    --card-back: #dbd9c9;
    --rule: #c9b98a;
    --wall-light: #eceeea;
    --wall-mid: #c9ccc4;
    --wall-warm: #bdbba6;
    --floor-light: #f4f1de;
    --floor-mid: #a7a38f;
  }
  * { margin: 0; padding: 0; box-sizing: border-box; }
  html, body {
    width: 1200px; height: 1000px; overflow: hidden;
    background: var(--page);
    font-family: "Cabin", "Gill Sans", sans-serif;
  }
  .canvas { position: relative; width: 1200px; height: 1000px; }

  .card {
    position: absolute;
    width: 605px; height: 347px;
    border: 1.5px solid var(--ink);
    overflow: hidden;
  }
  .card--front { left: 125px; top: 115px; }
  .card--back { left: 441px; top: 549px; background: var(--card-back); }

  /* front: interior scene fill */
  .front-scene {
    position: absolute; inset: 0;
    background:
      linear-gradient(180deg, transparent 0%, transparent 60%, var(--floor-light) 72%, var(--floor-mid) 100%),
      linear-gradient(90deg, var(--wall-light) 0%, var(--wall-mid) 45%, var(--wall-warm) 70%, var(--wall-light) 100%);
  }
  .wordmark {
    position: absolute;
    font-weight: 600;
    color: var(--logo);
    letter-spacing: 1px;
    line-height: 1;
  }
  .card--front .wordmark { left: 120px; top: 122px; font-size: 96px; }

  /* back: photo strips */
  .strip { position: absolute; }
  .strip--vertical {
    left: 103px; top: 0; width: 52px; height: 100%;
    background: linear-gradient(180deg, var(--wall-mid) 0%, var(--wall-light) 55%, var(--floor-mid) 75%, var(--floor-light) 100%);
    border-left: 1px solid var(--rule); border-right: 1px solid var(--rule);
  }
  .strip--band {
    left: 0; top: 171px; width: 379px; height: 42px;
    background: linear-gradient(180deg, var(--wall-mid) 0%, var(--wall-light) 70%, var(--floor-mid) 100%);
    border-top: 1px solid var(--rule); border-bottom: 1px solid var(--rule);
  }
  .strip--band-right {
    left: 379px; top: 171px; width: 226px; height: 42px;
    background: linear-gradient(90deg, #c8c5b0 0%, #9b9883 100%);
    border-top: 1px solid var(--rule); border-bottom: 1px solid var(--rule);
  }
  .back-glow {
    position: absolute; left: 0; top: 0; width: 605px; height: 171px;
    background: radial-gradient(ellipse at 45% 45%, #f2f1e8 0%, transparent 65%);
  }
  .card--back .wordmark { left: 20px; top: 44px; font-size: 90px; }

  .contact {
    position: absolute; left: 0; top: 226px; width: 605px;
    display: grid; grid-template-columns: 382px 1fr; column-gap: 14px;
    row-gap: 1px; font-size: 14px; line-height: 16.5px;
  }
  .contact dt { text-align: right; color: var(--label); font-weight: 400; }
  .contact dd { color: var(--ink); font-weight: 700; }
</style>
</head>
<body>
<div class="canvas">

  <section class="card card--front">
    <div class="front-scene" role="img" aria-label="Photograph of an empty sunlit room with white walls and pale wooden floorboards"></div>
    <div class="wordmark">Ostrevo</div>
  </section>

  <section class="card card--back">
    <div class="back-glow"></div>
    <div class="strip strip--vertical" role="img" aria-label="Slice of the empty room photograph showing wall and wooden floor"></div>
    <div class="strip strip--band" role="img" aria-label="Horizontal slice of the room photograph showing the wall base"></div>
    <div class="strip strip--band-right" role="img" aria-label="Slice of the room photograph showing a shaded wall"></div>
    <div class="wordmark">Ostrevo</div>
    <dl class="contact">
      <dt>Name:</dt><dd>Lucía Ostrini Varela</dd>
      <dt>Position:</dt><dd>Arquitecto</dd>
      <dt>Cell Phone :</dt><dd>+56 9 5550 1234</dd>
      <dt>E-mail address:</dt><dd>lostrini@ostrevo-studio.example</dd>
      <dt>website URL:</dt><dd>www.ostrevo-studio.example</dd>
    </dl>
  </section>

</div>
</body>
</html>
```